BRELM - Letterhead

Willowmere Institute of Letters and Crafts (BRELM) is a non-profit organization that operates two tuition-free public schools - BRELM Elementary for grades K to 5th and BRELM College Prep for grades 6-12.

We are looking for a letterhead primarily to be used on Google Docs and Microsoft Word. Attached are two versions of our logo. One with our name spelled out and one with the acronym.

For Letterhead, we would like 3 addresses listed:

BRELM HQ
41872 Hollow Brook Lane, Suite 308
Fernhollow, CA 90421

BRELM Elementary (K-5)
18460 Marsh Ridge Boulevard
Fernhollow, CA 90421

BRELM College Prep (6-12)
27314 Del Sol Terrace
Alder Cove, CA 90436

Our Phone Number is (555) 418-7062
Our Fax Number is the same (555) 418-7062

Our website is www.brelmschools.org

Target Market(s)

Education

Industry/Entity Type

Education

Font styles to use
Sans Serif

Colors
0054AA
0677BA
7BADD7
CADEEF
E8F1F8

Requirements
Must have
• Logo, Address, Phone Number, Website.
Nice to have
• Modern and clean design.
Should not have
• Prefer that there is no bleed -- the letterhead will mostly be used in PDF format however sometimes it will be printed and our printers can not do a full bleed

```html
<!DOCTYPE html>
<html lang="en">
<head>
<meta charset="utf-8">
<title>BRELM Letterhead</title>
<link href="https://fonts.googleapis.com/css2?family=Poppins:wght@300;400;500;700&display=swap" rel="stylesheet">
<style>
  :root {
    --yellow: #f7c81e;
    --orange: #ff6446;
    --green: #0e9a44;
    --sky: #0985cc;
    --navy: #0e3fa8;
    --brand: #1a4a9c;
    --ink: #3a3a3a;
    --dark: #1e1e1e;
    --faint: #ececec;
  }
  * { margin: 0; padding: 0; box-sizing: border-box; }
  html, body { width: 927px; height: 1200px; overflow: hidden; background: #fff; }
  body { font-family: "Poppins", sans-serif; color: var(--ink); }
  .sheet { position: relative; width: 927px; height: 1200px; overflow: hidden; background: #fff; }

  .brand { position: absolute; left: 38px; top: 38px; display: flex; align-items: center; gap: 26px; }
  .brand-dot { width: 78px; height: 78px; border-radius: 50%; background: var(--orange); }
  .brand-name { font-weight: 700; font-size: 23px; line-height: 30px; color: var(--brand); }

  .meta { position: absolute; left: 724px; top: 46px; font-size: 14px; color: var(--dark); letter-spacing: -0.4px; }
  .meta p { height: 38px; }

  .stripe { position: absolute; display: flex; flex-direction: column; border-radius: 6px; overflow: hidden; }
  .stripe span { flex: 1; }
  .stripe span:nth-child(1) { background: var(--yellow); }
  .stripe span:nth-child(2) { background: var(--orange); }
  .stripe span:nth-child(3) { background: var(--green); }
  .stripe span:nth-child(4) { background: var(--sky); }
  .stripe span:nth-child(5) { background: var(--navy); }
  .stripe-top { left: 896px; top: 10px; width: 6px; height: 134px; }
  .stripe-body { left: 37px; top: 163px; width: 13px; height: 616px; }
  .stripe-address { left: 37px; top: 936px; width: 13px; height: 225px; }

  .backdrop-name { position: absolute; left: 0; width: 927px; top: 665px; text-align: center;
    font-weight: 500; font-size: 140px; letter-spacing: 4px; color: var(--faint); }

  .letter { position: absolute; left: 80px; top: 212px; width: 817px; font-size: 14.6px; line-height: 27.2px; font-weight: 300; color: #2e2e2e; }
  .letter .recipient { margin-bottom: 24px; }
  .letter .salutation { margin-bottom: 16px; }
  .letter .message { text-align: justify; margin-bottom: 27px; letter-spacing: 0.25px; }
  .letter .signature-line { margin-top: 34px; width: 158px; border-bottom: 1px solid var(--ink); height: 10px; margin-bottom: 8px; }

  .contact { position: absolute; left: 36px; top: 786px; list-style: none; font-size: 15px; color: var(--dark); }
  .contact li { display: flex; align-items: center; gap: 14px; height: 43.5px; }
  .contact svg { width: 18px; height: 18px; }

  .addresses { position: absolute; left: 69px; top: 947px; font-size: 15px; line-height: 18.5px; color: var(--dark); font-style: normal; }
  .addresses .site { margin-bottom: 17px; }
  .addresses h3 { font-weight: 400; font-size: 15px; }
  .site-hq h3 { color: var(--navy); }
  .site-elementary h3 { color: var(--sky); }
  .site-prep h3 { color: var(--orange); }
</style>
</head>
<body>
<div class="sheet">
  <div class="backdrop-name" aria-hidden="true">BRELM</div>

  <header class="brand">
    <div class="brand-dot"></div>
    <div class="brand-name">Willowmere Institute<br>of Letters and Crafts</div>
  </header>

  <div class="meta">
    <p>Date:____________</p>
    <p>Ref #:____________</p>
  </div>

  <div class="stripe stripe-top"><span></span><span></span><span></span><span></span><span></span></div>
  <div class="stripe stripe-body"><span></span><span></span><span></span><span></span><span></span></div>

  <main class="letter">
    <p class="recipient">To:<br>The Director<br>ABC EFG, HIJK</p>
    <p class="salutation">Respected Sir/Madam,</p>
    <p class="message">Lorem Ipsum is simply dummy text of the printing and typesetting industry. Lorem Ipsum has been the industry's standard dummy text ever since the 1500s, when an unknown printer took a galley of type and scrambled it to make a type specimen book. It has survived not only five centuries, but also the leap into electronic typesetting, remaining essentially unchanged. It was popularised in the 1960s with the release of Lettrawell sheets containing Lorem Ipsum passages, and more recently with desktop publishing software like Folio PageCraft including versions of Lorem Ipsum.</p>
    <p>Regards</p>
    <div class="signature-line"></div>
    <p>PRINCIPLE</p>
  </main>

  <ul class="contact">
    <li>
      <svg viewBox="0 0 18 18" aria-label="Phone"><circle cx="9" cy="9" r="9" fill="var(--yellow)"/><path d="M6 4.5l1.6 2-0.9 1.2c0.6 1.3 1.5 2.2 2.8 2.8l1.2-0.9 2 1.6-0.9 1.6c-3.4 0-6.6-3.2-6.6-6.6z" fill="#222"/></svg>
      <span>(555) 418-7062</span>
    </li>
    <li>
      <svg viewBox="0 0 18 18" aria-label="Fax"><circle cx="9" cy="9" r="9" fill="var(--sky)"/><rect x="6" y="4" width="6" height="3" fill="#fff"/><rect x="4" y="7" width="10" height="5" rx="1" fill="#fff"/><rect x="6" y="10.5" width="6" height="3.5" fill="#fff" stroke="var(--sky)" stroke-width="0.8"/></svg>
      <span>(555) 418-7062</span>
    </li>
    <li>
      <svg viewBox="0 0 18 18" aria-label="Website"><circle cx="9" cy="9" r="9" fill="#f5a623"/><g fill="none" stroke="#fff" stroke-width="1"><circle cx="9" cy="9" r="5"/><ellipse cx="9" cy="9" rx="2.2" ry="5"/><path d="M4 9h10M5 6.5h8M5 11.5h8"/></g></svg>
      <span>www.brelmschools.org</span>
    </li>
  </ul>

  <div class="stripe stripe-address"><span></span><span></span><span></span><span></span><span></span></div>

  <address class="addresses">
    <div class="site site-hq">
      <h3>BRELM HQ</h3>
      <p>41872 Hollow Brook Lane, Suite 308<br>Fernhollow, CA 90421</p>
    </div>
    <div class="site site-elementary">
      <h3>BRELM Elementary (K-5)</h3>
      <p>18460 Marsh Ridge Boulevard<br>Fernhollow, CA 90421</p>
    </div>
    <div class="site site-prep">
      <h3>BRELM College Prep (6-12)</h3>
      <p>27314 Del Sol Terrace<br>Alder Cove, CA 90436</p>
    </div>
  </address>
</div>
</body>
</html>
```